Corvane Holdings , new business card design

investment firm with corporate clients . need double sided business card , vertical and horizontal options ,logo must be clear. prefer pantone colors only and sharp design. website also www.corvane-example.ae

Khalid Bin Rashed
Managing Director
Tel. +971 4 000 3829
Mobile +971 50 000 4172
khalid@corvane-example.ae
Palm Crest Tower, officw 18-B07, Qasr Gardens, Dubai

Contact Information for Business Card

Khalid Bin Rashed
Managing Director

Font styles to use
Serif

Colors

Designer to choose colors to be used in the design.

```html
<!DOCTYPE html>
<html lang="en">
<head>
<meta charset="utf-8">
<title>Corvane Holdings – Business Card</title>
<link rel="stylesheet" href="https://fonts.googleapis.com/css2?family=Lato:wght@300;400;700&display=swap">
<style>
  :root {
    --steel-blue: #4a74a0;
    --navy: #13296b;
    --ink: #1c1c1c;
    --text-grey: #333a44;
    --paper: #ffffff;
    --backdrop: #e9ebee;
  }
  * { margin: 0; padding: 0; box-sizing: border-box; }
  html, body {
    width: 1200px; height: 960px; overflow: hidden;
    background: var(--backdrop);
    font-family: "Lato", Arial, sans-serif;
  }
  .canvas { position: relative; width: 1200px; height: 960px; }
  .card {
    position: absolute; left: 240px; width: 720px; height: 411px;
    box-shadow: 0 6px 20px rgba(0,0,0,0.18);
    overflow: hidden;
  }
  .card--front { top: 46px; background: var(--steel-blue); }
  .card--back { top: 503px; background: var(--paper); }

  .brand-name {
    font-weight: 300; text-transform: uppercase; text-align: center;
    letter-spacing: 0.18em; line-height: 1;
  }
  .card--front .brand-name {
    position: absolute; top: 128px; left: 0; right: 0;
    font-size: 46px; color: var(--ink);
  }
  .card--front .website {
    position: absolute; top: 236px; left: 0; right: 0; text-align: center;
    color: var(--paper); font-size: 21px; letter-spacing: 0.12em;
  }
  .card--back .brand-name {
    position: absolute; top: 62px; left: 0; right: 0;
    font-size: 42px; color: var(--ink);
  }

  .person {
    position: absolute; top: 176px; left: 40px; width: 310px; text-align: right;
  }
  .person__name { color: var(--navy); font-weight: 700; font-size: 17px; letter-spacing: 0.02em; text-transform: uppercase; }
  .person__title { color: var(--navy); font-size: 16px; text-transform: uppercase; margin-top: 2px; }
  .person__address { color: var(--text-grey); font-size: 16px; line-height: 1.35; margin-top: 8px; }

  .divider {
    position: absolute; left: 368px; top: 172px; width: 1px; height: 104px;
    background: var(--navy);
  }
  .contacts { position: absolute; top: 170px; left: 384px; list-style: none; }
  .contacts li {
    display: flex; align-items: center; gap: 8px;
    color: var(--text-grey); font-size: 15.5px; height: 26px;
  }
  .contacts svg { width: 14px; height: 14px; fill: var(--navy); flex: none; }

  .waves { position: absolute; left: 0; bottom: 0; width: 720px; height: 411px; }
</style>
</head>
<body>
<main class="canvas">

  <section class="card card--front" aria-label="Card front">
    <div class="brand-name">Corvane Holdings</div>
    <div class="website">www.corvane-example.ae</div>
  </section>

  <section class="card card--back" aria-label="Card back">
    <div class="brand-name">Corvane Holdings</div>

    <div class="person">
      <div class="person__name">Khalid Bin Rashed</div>
      <div class="person__title">Managing Director</div>
      <div class="person__address">Palm Crest Tower, officw 18-B07<br>Qasr Gardens, Dubai</div>
    </div>

    <div class="divider"></div>

    <ul class="contacts">
      <li><svg viewBox="0 0 16 16" aria-hidden="true"><path d="M3.5 1.5l2.5 0 1 3.5-1.6 1.2a8 8 0 0 0 4.4 4.4L11 9l3.5 1v2.5c0 1-1 2-2 2C6.5 14.5 1.5 9.5 1.5 3.5c0-1 1-2 2-2z"/></svg>+971 4 000 3829</li>
      <li><svg viewBox="0 0 16 16" aria-hidden="true"><path d="M4.5 0.5h7a1 1 0 0 1 1 1v13a1 1 0 0 1-1 1h-7a1 1 0 0 1-1-1v-13a1 1 0 0 1 1-1zM5 2.5v9h6v-9zM8 12.5a1 1 0 1 0 0 2 1 1 0 0 0 0-2z"/></svg>+971 50 000 4172</li>
      <li><svg viewBox="0 0 16 16" aria-hidden="true"><path d="M1 3.5h14v9H1zM2 4.5l6 4.5 6-4.5v-0.2H2z" fill-rule="evenodd"/></svg>khalid@corvane-example.ae</li>
      <li><svg viewBox="0 0 16 16" aria-hidden="true"><path d="M8 1a7 7 0 1 0 0 14A7 7 0 0 0 8 1zm0 1.4c.8.8 1.5 2.2 1.7 3.9H6.3C6.5 4.6 7.2 3.2 8 2.4zM2.5 7.3h2.8a10 10 0 0 0 .5 2.8H3a5.6 5.6 0 0 1-.5-2.8zm0-1h.5-.5zM3.1 6.3a5.6 5.6 0 0 1 3-3.5 8 8 0 0 0-1.1 3.5zm3.2 1h3.4a9 9 0 0 1-.5 2.8H6.8a9 9 0 0 1-.5-2.8zm4.4-1a8 8 0 0 0-1.1-3.5 5.6 5.6 0 0 1 3 3.5zm0 1h2.8a5.6 5.6 0 0 1-.5 2.8h-2.8a10 10 0 0 0 .5-2.8zM3.6 11.1h2.5a7 7 0 0 0 .9 2.3 5.6 5.6 0 0 1-3.4-2.3zm3.5 0h1.8A6 6 0 0 1 8 13.4a6 6 0 0 1-.9-2.3zm2.8 0h2.5a5.6 5.6 0 0 1-3.4 2.3 7 7 0 0 0 .9-2.3z"/></svg>www.corvane-example.ae</li>
    </ul>

    <svg class="waves" viewBox="0 0 720 411" aria-hidden="true">
      <path d="M0 318 C 170 410, 400 330, 720 262 L720 411 L0 411 Z" fill="var(--steel-blue)"/>
      <path d="M0 352 C 190 420, 420 320, 720 268 L720 411 L0 411 Z" fill="var(--paper)"/>
      <path d="M0 358 C 200 424, 430 330, 720 276 L720 411 L0 411 Z" fill="var(--navy)"/>
    </svg>
  </section>

</main>
</body>
</html>
```